Website Design for recruiting company

We need a homepage mockup for a recruiting company focused on the legal industry. Use your creative talent to come up with something visually appeal and professional for this web-site.

We'd really like to see the maze from the logo incorporated into the design somehow. Please use the website mockup provided as inspiration for this project. We really like the layout and photos!

Target Market(s)

lawyers

Industry/Entity Type

Legal

Number of Pages Required

1 page

Font styles to use
Sans Serif

```html
<!DOCTYPE html>
<html lang="en">
<head>
<meta charset="utf-8">
<title>Harbor Legal Search</title>
<link rel="stylesheet" href="https://fonts.googleapis.com/css2?family=Poppins:ital,wght@0,300;0,400;0,500;0,600;0,700;1,600&display=swap">
<style>
:root{
  --navy:#1f3f75;
  --hero-a:#5f7bab;
  --hero-b:#4a6699;
  --tile:#2f5088;
  --plum-a:#4f3d4e;
  --plum-b:#766373;
  --band-a:#6d5a6e;
  --band-b:#8a7889;
  --footer:#2a2a2a;
  --footer-line:#3d3d3d;
  --muted:#8d8d8d;
  --white:#ffffff;
  --ink:#222222;
}
*{box-sizing:border-box;margin:0;padding:0}
html,body{width:778px;height:1200px;overflow:hidden;background:var(--white)}
body{font-family:'Poppins',sans-serif;color:var(--ink);position:relative}
.abs{position:absolute}

/* header + hero */
.hero{left:0;top:0;width:778px;height:261px;background:linear-gradient(160deg,var(--hero-a),var(--hero-b))}
.topbar{left:0;top:0;width:778px;height:34px;border-bottom:1px solid rgba(255,255,255,.25)}
.brand{display:flex;align-items:center;gap:7px;color:var(--white);font-weight:300;font-size:10.5px;letter-spacing:.1px}
.brand .dot{width:26px;height:26px;border-radius:50%;border:1.5px solid rgba(255,255,255,.8)}
.topbar .brand{left:152px;top:4px}
.nav{left:358px;top:12px;display:flex;gap:20px;font-size:6px;color:var(--white);font-weight:500}
.nav-divider{left:580px;top:0;width:1px;height:34px;background:rgba(255,255,255,.25)}
.explore{left:593px;top:11px;font-size:6px;color:var(--white);font-weight:500;display:flex;align-items:center;gap:5px}
.hero-title{left:0;width:778px;text-align:center;color:var(--white);font-weight:700}
.hero-title.one{top:120px;font-size:25px;letter-spacing:.3px}
.hero-title.two{top:158px;font-size:16px}

/* about */
.about-title{left:0;top:290px;width:778px;text-align:center;color:var(--navy);font-weight:700;font-size:12.5px}
.about-text{left:214px;top:314px;width:350px;text-align:center;font-size:6.6px;line-height:12.2px}
.about-text em{font-weight:600}

.feature-photo{left:274px;top:390px;width:352px;height:207px;background:linear-gradient(120deg,#b7c3cf,#6d8395 55%,#3f5d6a)}
.news{left:152px;top:489px;width:231px;height:127px;background:linear-gradient(90deg,var(--plum-a),var(--plum-b));color:var(--white)}
.news h2{position:absolute;left:24px;top:22px;font-size:12px;font-weight:600}
.news p{position:absolute;left:24px;top:45px;width:180px;font-size:6.8px;line-height:12px}
.btn{display:flex;align-items:center;justify-content:center;background:var(--white);font-size:6.2px;font-weight:600;color:#5a4a5a}
.news .btn{position:absolute;left:22px;top:82px;width:85px;height:23px}

.tiles{left:152px;top:640px;display:flex;gap:7px}
.tile{width:89px;height:81px;background:linear-gradient(150deg,#4a6ca0,var(--tile));display:flex;flex-direction:column;align-items:center;justify-content:center;gap:6px;color:var(--white);font-size:6.5px;font-weight:600}

/* employers */
.employers{left:0;top:756px;width:778px;height:220px;background:linear-gradient(180deg,var(--band-b),var(--band-a))}
.emp-kicker{left:0;top:808px;width:778px;text-align:center;color:var(--white);font-weight:600;font-size:12px}
.emp-text{left:254px;top:833px;width:270px;text-align:center;color:var(--white);font-size:6.6px;line-height:12.2px}
.emp-title{left:0;top:862px;width:778px;text-align:center;color:var(--white);font-weight:700;font-size:20.5px}
.emp-btn{left:347px;top:902px;width:84px;height:23px}

/* footer */
.footer{left:0;top:976px;width:778px;height:224px;background:var(--footer)}
.footer-top{left:0;top:976px;width:778px;height:46px;border-bottom:1px solid var(--footer-line)}
.footer-top .brand{left:152px;top:11px}
.footer-divider{left:462px;top:976px;width:1px;height:46px;background:var(--footer-line)}
.follow{left:476px;top:992px;display:flex;align-items:center;gap:12px;color:var(--white);font-size:6.2px;font-weight:600}
.socials{display:flex;gap:4px}
.socials span{width:17px;height:17px;border-radius:50%;border:1px solid #cfcfcf}
.col{top:1044px;color:var(--muted);font-size:5.8px}
.col h3{color:var(--white);font-weight:400;font-size:7.6px;margin-bottom:8px}
.col li{list-style:none;margin-bottom:8.6px}
.newsletter p{width:150px;line-height:9.6px}
.field{position:absolute;top:49px;left:-1px;width:114px;height:20px;background:#333;border:1px solid #3a3a3a;font-size:5.4px;color:#888;padding:6px 6px}
.subscribe{position:absolute;top:49px;left:117px;width:49px;height:20px;background:#7a6478;color:var(--white);font-size:5.6px;font-weight:600;display:flex;align-items:center;justify-content:center;border-radius:1px}
.copy-line{left:0;top:1157px;width:778px;height:1px;background:var(--footer-line)}
.copy{left:0;top:1174px;width:778px;text-align:center;color:var(--muted);font-size:5.4px}
</style>
</head>
<body>

<div class="abs hero" role="img" aria-label="Photo of colleagues talking in a bright office, tinted blue"></div>
<header class="abs topbar">
  <div class="abs brand"><span class="dot"></span>harbor legal search</div>
  <nav class="abs nav"><span>Find a Job</span><span>Employers</span><span>About Us</span><span>Contact</span></nav>
  <div class="abs nav-divider"></div>
  <div class="abs explore">Explore
    <svg width="8" height="8" viewBox="0 0 10 10"><circle cx="4" cy="4" r="3" fill="none" stroke="#fff" stroke-width="1.3"/><line x1="6.3" y1="6.3" x2="9" y2="9" stroke="#fff" stroke-width="1.3"/></svg>
  </div>
</header>
<h1 class="abs hero-title one">START HERE,</h1>
<p class="abs hero-title two">LET OUR EXPERIENCE GUIDE YOU</p>

<h2 class="abs about-title">ABOUT US</h2>
<p class="abs about-text">Harbor Legal Search focuses on the permanent placement of attorneys with law firms and corporations in the New England area. Founded in 1982, Harbor Legal Search is the oldest attorney search firm in New England, and is ranked the number one legal recruiter in New England in the most recent survey conducted by <em><i>The Legal Ledger</i></em> .</p>

<div class="abs feature-photo" role="img" aria-label="Photo of a man working on a laptop on a sofa by a window"></div>
<section class="abs news">
  <h2>WHAT’S NEW</h2>
  <p>Below are our most recent listings. All positions are in the greater Boston area unless otherwise noted.</p>
  <a class="btn">SEARCH JOBS</a>
</section>

<div class="abs tiles">
  <div class="tile">
    <svg width="22" height="22" viewBox="0 0 24 24" fill="none" stroke="#fff" stroke-width="1.3"><rect x="8" y="3" width="9" height="6" transform="rotate(40 12 6)"/><line x1="10" y1="11" x2="4" y2="17"/><rect x="4" y="19" width="12" height="3"/></svg>
    <span>JOB TITLE (5)</span>
  </div>
  <div class="tile">
    <svg width="22" height="22" viewBox="0 0 24 24" fill="none" stroke="#fff" stroke-width="1.3"><line x1="12" y1="3" x2="12" y2="20"/><line x1="4" y1="6" x2="20" y2="6"/><path d="M2 13l3-7 3 7z"/><path d="M16 13l3-7 3 7z"/><line x1="7" y1="21" x2="17" y2="21"/></svg>
    <span>JOB TITLE (5)</span>
  </div>
  <div class="tile">
    <svg width="22" height="22" viewBox="0 0 24 24" fill="none" stroke="#fff" stroke-width="1.3"><path d="M12 2l8 3v7c0 5-4 8-8 10-4-2-8-5-8-10V5z"/><path d="M12 8l1.2 2.6 2.8.3-2.1 1.9.6 2.8L12 14.2 9.5 15.6l.6-2.8L8 10.9l2.8-.3z"/></svg>
    <span>JOB TITLE (5)</span>
  </div>
  <div class="tile">
    <svg width="22" height="22" viewBox="0 0 24 24" fill="none" stroke="#fff" stroke-width="1.3"><path d="M6 10a6 6 0 0 1 12 0z"/><line x1="12" y1="1" x2="12" y2="4"/><line x1="8" y1="12" x2="8" y2="19"/><line x1="11" y1="12" x2="11" y2="19"/><line x1="14" y1="12" x2="14" y2="19"/><line x1="17" y1="12" x2="17" y2="19"/><rect x="2" y="19" width="20" height="3"/></svg>
    <span>JOB TITLE (5)</span>
  </div>
  <div class="tile">
    <svg width="22" height="22" viewBox="0 0 24 24" fill="none" stroke="#fff" stroke-width="1.3"><path d="M5 2h10l4 4v16H5z"/><line x1="8" y1="9" x2="16" y2="9"/><line x1="8" y1="12" x2="16" y2="12"/><line x1="8" y1="15" x2="13" y2="15"/></svg>
    <span>JOB TITLE (5)</span>
  </div>
</div>

<div class="abs employers" role="img" aria-label="Photo of a team meeting around a table, tinted plum"></div>
<h2 class="abs emp-kicker">FOR EMPLOYERS</h2>
<p class="abs emp-text">Our unparalleled recruiting industry and legal experience have generated an extensive network of contacts throughout the legal community.</p>
<p class="abs emp-title">FIND THE RIGHT CANDIDATE</p>
<a class="abs btn emp-btn">START HERE</a>

<footer class="abs footer"></footer>
<div class="abs footer-top">
  <div class="abs brand"><span class="dot"></span>harbor legal search</div>
</div>
<div class="abs footer-divider"></div>
<div class="abs follow">FOLLOW US:
  <div class="socials"><span></span><span></span><span></span><span></span><span></span></div>
</div>

<div class="abs col" style="left:152px"><h3>For Candidates</h3><ul><li>Browse Jobs</li><li>Browse Categories</li><li>Candidate Dashboard</li><li>Job Alerts</li><li>MY Bookmarks</li></ul></div>
<div class="abs col" style="left:237px"><h3>For Employees</h3><ul><li>Browse Candidates</li><li>Employer Dashboard</li><li>Add Job</li><li>Job Packages</li></ul></div>
<div class="abs col" style="left:318px"><h3>Other</h3><ul><li>Job Page</li><li>Job Page Alternative</li><li>Resume Page</li><li>Blog</li><li>Contact</li></ul></div>
<div class="abs col" style="left:398px"><h3>Legal</h3><ul><li>Privacy Policy</li><li>Terms of Use</li><li>FAQ</li></ul></div>
<div class="abs col newsletter" style="left:459px">
  <h3><svg width="8" height="6" viewBox="0 0 10 8" style="margin-right:4px"><rect x=".5" y=".5" width="9" height="7" fill="none" stroke="#fff"/><path d="M.5 .5l4.5 4 4.5-4" fill="none" stroke="#fff"/></svg>Sign up for a Newsletter</h3>
  <p>Weekly breaking news, analysis and cutting edge advices on job searching.</p>
  <div class="field">Enter your email here</div>
  <div class="subscribe">Subscribe</div>
</div>

<div class="abs copy-line"></div>
<p class="abs copy">harbor legal search © 2020. All rights reserved.</p>

</body>
</html>
```